Brackenford Lane Vineyard website

I need to have our website design done. It is an existing site www.brackenfordlane.com.au which is based on Wordpress which includes information and online purchasing of our wine. Logo and existing branding are to be maintained but website needs to be improved and open to recommendations for function extensions.

Target Market(s)

Wine drinkers and people wanting to visit or hold and event.
Aged from 25-55, men and women

Industry/Entity Type

Vineyard

Number of Pages Required

5+ page

Font styles to use
Sans Serif

Requirements
Must have
• Incorporate existing logos and styling from bottles.
• See existing website www.brackenfordlane.com.au

```html
<!DOCTYPE html>
<html lang="en">
<head>
<meta charset="utf-8">
<title>Brackenford Lane Vineyard</title>
<link href="https://fonts.googleapis.com/css2?family=Lato:wght@400;700&family=Open+Sans:wght@400;600&display=swap" rel="stylesheet">
<style>
:root{
  --green:#2a8a16;
  --green-dark:#1f6e0e;
  --red:#d0121b;
  --ink:#222;
  --muted:#666;
  --line:#e3e3e3;
  --light:#f3f3f3;
  --footer:#1c1c1c;
  --footer-bottom:#141414;
  --footer-text:#9a9a9a;
  --white:#fff;
}
*{box-sizing:border-box;margin:0;padding:0}
html,body{width:1200px;height:2514px;overflow:hidden;background:var(--white)}
body{font-family:"Lato",sans-serif;color:var(--ink);position:relative}

/* hero */
.hero{position:absolute;left:0;top:0;width:1200px;height:608px;overflow:hidden}
.hero-photo{position:absolute;inset:0;background:linear-gradient(180deg,#6a6a52 0%,#4b5230 35%,#2f3a1c 65%,#1b2210 100%)}
.hero-glow{position:absolute;inset:0;background:radial-gradient(ellipse at 78% 8%,rgba(255,236,190,.55),rgba(255,236,190,0) 45%)}
.nav{position:absolute;top:40px;left:162px;width:876px;height:26px;display:flex;align-items:center;color:var(--white);font-size:11px;font-weight:700;letter-spacing:.3px}
.nav-menu{display:flex;gap:18px;align-items:center}
.brand{position:absolute;left:50%;transform:translateX(-50%);top:-6px;text-align:center;font-weight:400;color:var(--white);letter-spacing:2px;line-height:1.25}
.brand-name{font-size:25px}
.brand-sub{font-size:13px;display:block}
.nav-tools{margin-left:auto;display:flex;gap:18px;align-items:center;font-weight:400;font-size:11px}
.nav-tools svg{fill:var(--white)}
.slide-arrow{position:absolute;top:298px;width:30px;height:30px;border:1.5px solid rgba(255,255,255,.8);border-radius:50%}
.slide-arrow.prev{left:52px}.slide-arrow.next{left:1118px}
.caption-band{position:absolute;left:0;top:478px;width:1200px;height:130px;background:rgba(0,0,0,.45)}
.caption{position:absolute;left:195px;top:494px;width:810px;font-family:"Open Sans",sans-serif;font-size:22px;line-height:29px;color:var(--white)}
.hero-wave{position:absolute;left:0;top:570px}

/* featured */
.section-title{text-align:center;font-size:24px;font-weight:700;letter-spacing:.3px}
.title-rule{display:block;margin:12px auto 0}
.featured-title{position:absolute;top:672px;left:0;width:1200px}
.pager{position:absolute;top:690px;height:30px;padding:0 12px;font-size:9px;line-height:30px;font-weight:700}
.pager.prev{left:162px;background:#eee;color:#bbb;border:1px solid #e4e4e4}
.pager.next{left:994px;background:var(--green);color:var(--white);outline:2px solid var(--green-dark);outline-offset:-4px}
.wine-card{position:absolute;top:756px;width:277px;height:427px;border:1px solid var(--line);background:var(--white)}
.wine-stage{position:absolute;left:0;top:0;width:100%;height:316px;background:radial-gradient(ellipse at 50% 45%,#ececec,#f8f8f8 70%)}
.card-actions{position:absolute;left:0;width:100%;top:210px;display:flex;justify-content:center;align-items:center;gap:10px}
.act{width:36px;height:36px;border-radius:50%;background:#e6e6e6;display:flex;align-items:center;justify-content:center}
.act.main{width:40px;height:40px;background:var(--white);box-shadow:0 0 0 3px #eaeaea}
.card-wave{position:absolute;left:0;top:290px}
.wine-name{position:absolute;top:345px;width:100%;text-align:center;font-family:"Open Sans",sans-serif;font-size:19px;font-weight:400;color:var(--ink)}
.wine-price{position:absolute;top:374px;width:100%;text-align:center;font-family:"Open Sans",sans-serif;font-size:19px;font-weight:600;color:var(--red)}

/* about */
.about{position:absolute;top:1253px;left:0;width:1200px;height:443px;background:linear-gradient(120deg,#e6e6e6,#f3f3f3 50%,#e9e9e9)}
.about-photo{position:absolute;left:162px;top:95px;width:426px;height:256px;background:linear-gradient(160deg,#5e6e42,#3f5126 55%,#7a6450);border:2px solid var(--white)}
.about-body{position:absolute;left:613px;top:84px;width:425px}
.about-body h2{font-family:"Open Sans",sans-serif;font-weight:400;font-size:26px;margin-bottom:12px}
.about-body p{font-size:11px;line-height:17.5px;color:var(--muted)}
.btn{position:absolute;top:317px;height:33px;padding:0 18px;font-size:10px;font-weight:700;line-height:33px;color:var(--white)}
.btn.buy{left:613px;background:var(--green)}
.btn.more{left:714px;background:#333}
.about-wave{position:absolute;left:0;top:403px}

/* features */
.features{position:absolute;top:1696px;left:0;width:1200px;height:267px;background:var(--light)}
.feature{position:absolute;top:44px;width:300px;text-align:center}
.feature+.feature{border-left:1px solid #e2e2e2}
.f-icon{width:38px;height:38px;border-radius:50%;background:var(--green);margin:0 auto;display:flex;align-items:center;justify-content:center}
.feature h3{font-family:"Open Sans",sans-serif;font-weight:600;font-size:18px;margin-top:12px}
.feature .rule{width:80px;height:1px;background:#d4d4d4;margin:8px auto 12px}
.feature p{font-size:11px;line-height:17.5px;color:var(--muted);width:240px;margin:0 auto}

/* newsletter */
.newsletter{position:absolute;top:1963px;left:0;width:1200px;height:222px}
.n-icon{position:absolute;left:585px;top:45px;width:30px;height:30px;border-radius:50%;background:var(--green);display:flex;align-items:center;justify-content:center}
.newsletter h2{position:absolute;top:90px;width:100%;text-align:center;font-family:"Open Sans",sans-serif;font-weight:400;font-size:25px}
.subscribe{position:absolute;left:162px;top:148px;width:876px;height:30px;display:flex;align-items:center}
.subscribe label{font-size:13px;font-weight:700;width:127px}
.field{height:30px;border:1px solid #ddd;font-size:9px;color:#999;padding-left:12px;line-height:28px}
.field.name{width:302px}.field.email{width:302px;margin-left:20px}
.submit{margin-left:20px;width:105px;height:30px;background:var(--green);color:var(--white);font-size:10px;font-weight:700;text-align:center;line-height:30px}

/* footer */
.footer{position:absolute;top:2185px;left:0;width:1200px;height:270px;background:var(--footer);color:var(--footer-text)}
.f-col{position:absolute;top:60px;width:200px}
.f-col h4{color:var(--white);font-size:10px;font-weight:700;letter-spacing:.3px;padding-bottom:14px;border-bottom:1px solid #333;margin-bottom:14px}
.f-col p{font-size:10px;line-height:16px}
.f-col ul{list-style:none}
.f-col li{font-size:10px;line-height:20px}
.f-col li::before{content:"•";margin-right:8px}
.socials{display:flex;gap:6px;margin-top:16px}
.socials span{width:16px;height:16px;background:#2b2b2b;border:1px solid #3a3a3a}
.socials span.on{background:var(--green)}
.contact-line{display:flex;gap:10px;font-size:9.5px;line-height:13px;margin-top:12px}
.contact-line i{flex:0 0 16px;height:16px;background:#2f2f2f;display:flex;align-items:center;justify-content:center}
.footer-bottom{position:absolute;top:2455px;left:0;width:1200px;height:59px;background:var(--footer-bottom);color:#8a8a8a;font-size:10px;text-align:center;line-height:59px}
</style>
</head>
<body>

<header class="hero">
  <div class="hero-photo" role="img" aria-label="Sunlit vineyard rows with wooden posts and a farmhouse at dusk"></div>
  <div class="hero-glow"></div>
  <nav class="nav">
    <div class="nav-menu">
      <svg width="12" height="11" viewBox="0 0 12 11"><path d="M6 0 0 5h2v6h3V7h2v4h3V5h2z" fill="#fff"/></svg>
      <span>WINE</span><span>EVENT</span><span>GALLERY</span><span>CONTACT US</span>
    </div>
    <div class="brand"><span class="brand-name">BRACKENFORD LANE</span><span class="brand-sub">VINEYARD</span></div>
    <div class="nav-tools">
      <span><svg width="12" height="10" viewBox="0 0 12 10"><path d="M0 3h12l-2 7H2z"/></svg> $00.00</span>
      <span>USD</span><span>ENGLISH</span>
      <span style="display:flex;gap:7px">
        <svg width="10" height="10" viewBox="0 0 10 10"><circle cx="5" cy="3" r="2.5"/><path d="M0 10a5 4 0 0 1 10 0z"/></svg>
        <svg width="10" height="10" viewBox="0 0 10 10"><circle cx="4" cy="4" r="3" fill="none" stroke="#fff" stroke-width="1.5"/><path d="M6 6l3.5 3.5" stroke="#fff" stroke-width="1.5"/></svg>
        <svg width="10" height="10" viewBox="0 0 10 10"><rect y="1" width="10" height="1.6"/><rect y="4.2" width="10" height="1.6"/><rect y="7.4" width="10" height="1.6"/></svg>
      </span>
    </div>
  </nav>
  <svg class="slide-arrow prev" viewBox="0 0 30 30"><path d="M17 9l-6 6 6 6" fill="none" stroke="#fff" stroke-width="1.5"/></svg>
  <svg class="slide-arrow next" viewBox="0 0 30 30"><path d="M13 9l6 6-6 6" fill="none" stroke="#fff" stroke-width="1.5"/></svg>
  <div class="caption-band"></div>
  <p class="caption">You’ll find our boutique vineyard a little way along the road high on the Lake Merrow Escarpment.</p>
  <svg class="hero-wave" width="1200" height="40" viewBox="0 0 1200 40"><path d="M0 40V38H480C540 38 550 8 600 8S660 38 720 38H1200V40Z" fill="#fff"/></svg>
</header>

<h2 class="section-title featured-title">FEATURED WINE
  <svg class="title-rule" width="100" height="8" viewBox="0 0 100 8"><path d="M0 4h46M54 4h46" stroke="#ccc"/><circle cx="50" cy="4" r="3" fill="none" stroke="#ccc"/></svg>
</h2>
<span class="pager prev">PREV</span>
<span class="pager next">NEXT</span>

<article class="wine-card" style="left:162px">
  <div class="wine-stage" role="img" aria-label="Product photo of the Riesling 2015 bottle"></div>
  <div class="card-actions">
    <span class="act"><svg width="12" height="12" viewBox="0 0 12 12"><circle cx="5" cy="5" r="3.5" fill="none" stroke="#2a8a16" stroke-width="1.6"/><path d="M7.5 7.5l3.5 3.5" stroke="#2a8a16" stroke-width="1.6"/></svg></span>
    <span class="act main"><svg width="18" height="14" viewBox="0 0 18 14"><path d="M1 4h16l-2.5 9h-11z" fill="#2a8a16"/><path d="M5 4l3-4M13 4l-3-4" stroke="#2a8a16" stroke-width="1.4"/></svg></span>
    <span class="act"><svg width="14" height="12" viewBox="0 0 14 12"><path d="M7 12 1 6a3.3 3.3 0 0 1 6-4 3.3 3.3 0 0 1 6 4z" fill="#2a8a16"/></svg></span>
  </div>
  <svg class="card-wave" width="275" height="30" viewBox="0 0 275 30"><path d="M0 30V24H95C115 24 120 10 137 10S160 24 180 24H275V30Z" fill="#fff"/></svg>
  <h3 class="wine-name">RIESLING 2015</h3>
  <p class="wine-price">$18.18</p>
</article>

<article class="wine-card" style="left:462px">
  <div class="wine-stage" role="img" aria-label="Product photo of the Pepper and Flint Red 2015 bottle"></div>
  <div class="card-actions">
    <span class="act"><svg width="12" height="12" viewBox="0 0 12 12"><circle cx="5" cy="5" r="3.5" fill="none" stroke="#2a8a16" stroke-width="1.6"/><path d="M7.5 7.5l3.5 3.5" stroke="#2a8a16" stroke-width="1.6"/></svg></span>
    <span class="act main"><svg width="18" height="14" viewBox="0 0 18 14"><path d="M1 4h16l-2.5 9h-11z" fill="#2a8a16"/><path d="M5 4l3-4M13 4l-3-4" stroke="#2a8a16" stroke-width="1.4"/></svg></span>
    <span class="act"><svg width="14" height="12" viewBox="0 0 14 12"><path d="M7 12 1 6a3.3 3.3 0 0 1 6-4 3.3 3.3 0 0 1 6 4z" fill="#2a8a16"/></svg></span>
  </div>
  <svg class="card-wave" width="275" height="30" viewBox="0 0 275 30"><path d="M0 30V24H95C115 24 120 10 137 10S160 24 180 24H275V30Z" fill="#fff"/></svg>
  <h3 class="wine-name">PEPPER AND FLINT RED 2015</h3>
  <p class="wine-price">$18.18</p>
</article>

<article class="wine-card" style="left:761px">
  <div class="wine-stage" role="img" aria-label="Product photo of the Sauvignon Blanc 2015 bottle"></div>
  <div class="card-actions">
    <span class="act"><svg width="12" height="12" viewBox="0 0 12 12"><circle cx="5" cy="5" r="3.5" fill="none" stroke="#2a8a16" stroke-width="1.6"/><path d="M7.5 7.5l3.5 3.5" stroke="#2a8a16" stroke-width="1.6"/></svg></span>
    <span class="act main"><svg width="18" height="14" viewBox="0 0 18 14"><path d="M1 4h16l-2.5 9h-11z" fill="#2a8a16"/><path d="M5 4l3-4M13 4l-3-4" stroke="#2a8a16" stroke-width="1.4"/></svg></span>
    <span class="act"><svg width="14" height="12" viewBox="0 0 14 12"><path d="M7 12 1 6a3.3 3.3 0 0 1 6-4 3.3 3.3 0 0 1 6 4z" fill="#2a8a16"/></svg></span>
  </div>
  <svg class="card-wave" width="275" height="30" viewBox="0 0 275 30"><path d="M0 30V24H95C115 24 120 10 137 10S160 24 180 24H275V30Z" fill="#fff"/></svg>
  <h3 class="wine-name">SAUVIGNON BLANC 2015</h3>
  <p class="wine-price">$18.18</p>
</article>

<section class="about">
  <div class="about-photo" role="img" aria-label="Aerial view of vineyard rows beside the winery shed"></div>
  <div class="about-body">
    <h2>ABOUT US</h2>
    <p>Lorem ipsum dolor sit amet, consectetuer adipiscing elit, sed diam nonummy nibhumils euismod tincidunt ut laoreet dolore magna aliquam erat volutpat. Ut wisi enim ad minim veniam, quis nostrud exerci tation ullamcorper suscipit lobortis nisl ut aliquip ex etilisun commodo consequat. Duis autem vel eum iriure dolor in hendrerit in vulputate velit esse molestie consequat, vel illum dolore eu feugiat nulla facilisis at vero eros et accumsan et iusto odio dignissim qui blandit praesent luptatum zzril delenit augue duis dolore te feugait nulla facilisi.</p>
  </div>
  <span class="btn buy">BUY NOW</span>
  <span class="btn more">LEARN MORE</span>
  <svg class="about-wave" width="1200" height="40" viewBox="0 0 1200 40"><path d="M0 40V38H500C550 38 560 14 600 14S650 38 700 38H1200V40Z" fill="#f3f3f3"/></svg>
</section>

<section class="features">
  <div class="feature" style="left:150px">
    <div class="f-icon"><svg width="12" height="16" viewBox="0 0 12 16"><path d="M6 16S0 9 0 6a6 6 0 0 1 12 0c0 3-6 10-6 10z" fill="#fff"/><circle cx="6" cy="6" r="2" fill="#2a8a16"/></svg></div>
    <h3>Events</h3><div class="rule"></div>
    <p>Lorem ipsum dolor sit amet, consectetuery adipiscing elit, sed diam nonummy nibhumils euismod tincidunt ut laoreet.</p>
  </div>
  <div class="feature" style="left:450px">
    <div class="f-icon"><svg width="16" height="13" viewBox="0 0 16 13"><rect x=".8" y=".8" width="14.4" height="11.4" fill="none" stroke="#fff" stroke-width="1.6"/><path d="M3 10l3.5-4 2.5 3 2-2 2 3z" fill="#fff"/><circle cx="11" cy="4" r="1.3" fill="#fff"/></svg></div>
    <h3>Gallery</h3><div class="rule"></div>
    <p>Lorem ipsum dolor sit amet, consectetuery adipiscing elit, sed diam nonummy nibhumils euismod tincidunt ut laoreet.</p>
  </div>
  <div class="feature" style="left:750px">
    <div class="f-icon"><svg width="18" height="13" viewBox="0 0 18 13"><circle cx="9" cy="3.5" r="3" fill="#fff"/><path d="M3 13a6 5 0 0 1 12 0z" fill="#fff"/><circle cx="3" cy="5" r="2" fill="#fff"/><circle cx="15" cy="5" r="2" fill="#fff"/></svg></div>
    <h3>Members</h3><div class="rule"></div>
    <p>Lorem ipsum dolor sit amet, consectetuery adipiscing elit, sed diam nonummy nibhumils euismod tincidunt ut laoreet.</p>
  </div>
</section>

<section class="newsletter">
  <div class="n-icon"><svg width="13" height="10" viewBox="0 0 13 10"><rect width="13" height="10" rx="1" fill="#fff"/><path d="M0 1l6.5 5L13 1" fill="none" stroke="#2a8a16" stroke-width="1.3"/></svg></div>
  <h2>NEWSLETTER</h2>
  <div class="subscribe">
    <label>Subscribe to us</label>
    <span class="field name">Enter your name</span>
    <span class="field email">Enter your email address</span>
    <span class="submit">SUBMIT</span>
  </div>
</section>

<footer class="footer">
  <div class="f-col" style="left:162px">
    <h4>ABOUT US</h4>
    <p>Lorem ipsum dolor sit amet eusiodim consectuer adipiscing elit, sed diam nonummy acces sanitem nibhumils euismod tincidunt ut laoreetos dolore magna.</p>
    <div class="socials"><span></span><span class="on"></span><span></span><span></span><span></span></div>
  </div>
  <div class="f-col" style="left:387px">
    <h4>MY ACCOUNT</h4>
    <ul><li>Home</li><li>About Us</li><li>Address</li><li>Discount</li><li>Order History</li><li>My Credit Slip</li></ul>
  </div>
  <div class="f-col" style="left:612px">
    <h4>OUR SERVICE</h4>
    <ul><li>Shipping &amp; Return</li><li>International Shipping</li><li>Secure Shopping</li><li>Affiliates</li><li>Careers</li><li>FAQ</li></ul>
  </div>
  <div class="f-col" style="left:837px">
    <h4>CONTACT US</h4>
    <p>Lorem ipsum dolor sit amet, consectetuer adipiscing elit.</p>
    <div class="contact-line"><i><svg width="8" height="10" viewBox="0 0 8 10"><path d="M4 10S0 6 0 4a4 4 0 0 1 8 0c0 2-4 6-4 6z" fill="#999"/></svg></i><span>12 Brackenford Lane - Millbrook - NSW - 2699 - Australia</span></div>
    <div class="contact-line"><i><svg width="9" height="7" viewBox="0 0 9 7"><rect width="9" height="7" fill="#999"/><path d="M0 0l4.5 4L9 0" fill="none" stroke="#2f2f2f"/></svg></i><span>wine@brackenfordlane.com.au</span></div>
    <div class="contact-line"><i><svg width="9" height="9" viewBox="0 0 9 9"><path d="M1 0h2l1 2.5-1.3 1a5 5 0 0 0 2.8 2.8l1-1.3L9 6v2a1 1 0 0 1-1 1A8 8 0 0 1 0 1a1 1 0 0 1 1-1z" fill="#999"/></svg></i><span>+61 400 555 017</span></div>
  </div>
</footer>
<div class="footer-bottom">Copyright © yoursite 2016. All Right Reserved</div>

</body>
</html>
```